Property Management Company Business Cards

Need business cards for a property management company located in Michigan. We manage houses for clients all over the world. Young and modern company, looking for eye catching design. Please work with the attached logo.

Industry/Entity Type

Property Management

Requirements
Must have
• Need lines for address, telephone number, fax number, web site.

Also lines for name, and job title

```html
<!DOCTYPE html>
<html lang="en">
<head>
<meta charset="utf-8">
<title>Lakeview Global Management – Business Cards</title>
<link rel="stylesheet" href="https://fonts.googleapis.com/css2?family=Roboto+Condensed:wght@400;700&family=Roboto:wght@300;400&display=swap">
<style>
  :root {
    --page-bg: #ffffff;
    --card-front: #ffffff;
    --card-border: #c9c9c9;
    --card-back: #3b3a3a;
    --ink-dark: #3a3a3a;
    --ink-mid: #555555;
    --accent-blue: #4aa3e8;
    --accent-blue-soft: #7fbcf0;
    --watermark-light: #ececec;
    --watermark-dark: #454444;
    --divider: #4a4a4a;
  }
  * { margin: 0; padding: 0; box-sizing: border-box; }
  html, body {
    width: 885px; height: 1200px; overflow: hidden;
    background: var(--page-bg);
  }
  .sheet { position: relative; width: 885px; height: 1200px; }

  .card {
    position: absolute;
    border-radius: 30px;
    overflow: hidden;
  }
  .card--front {
    left: 142px; top: 124px; width: 740px; height: 442px;
    background: var(--card-front);
    border: 2px solid var(--card-border);
  }
  .card--back {
    left: 136px; top: 655px; width: 744px; height: 520px;
    background: var(--card-back);
  }

  .watermark { position: absolute; border-radius: 50%; }
  .card--front .watermark {
    left: -40px; top: -70px; width: 300px; height: 300px;
    border: 44px solid var(--watermark-light);
  }
  .card--back .watermark {
    left: -40px; top: 150px; width: 330px; height: 330px;
    border: 48px solid var(--watermark-dark);
  }

  .holder {
    position: absolute; right: 60px; top: 100px; text-align: right;
    font-family: "Roboto", sans-serif;
  }
  .holder__name {
    font-weight: 300; font-size: 31px; color: var(--accent-blue-soft);
    letter-spacing: 0.5px;
  }
  .holder__position {
    font-weight: 400; font-size: 19px; color: var(--accent-blue);
    margin-top: 4px;
  }

  .brand-front {
    position: absolute; left: 68px; top: 292px;
    display: flex; align-items: center; gap: 12px;
  }
  .brand-front__mark {
    width: 40px; height: 40px; border-radius: 50%;
    background: var(--ink-dark);
  }
  .brand-front__name {
    font-family: "Roboto Condensed", sans-serif; font-weight: 700;
    color: var(--ink-dark); line-height: 1;
  }
  .brand-front__line1 { font-size: 30px; display: block; }
  .brand-front__line2 { font-size: 11px; letter-spacing: 9.2px; display: block; margin-top: 3px; }

  .divider {
    position: absolute; left: 416px; top: 282px; width: 2px; height: 82px;
    background: var(--divider);
  }

  .contact {
    position: absolute; left: 450px; top: 280px; list-style: none;
    font-family: "Roboto", sans-serif; font-size: 18px; color: var(--ink-dark);
  }
  .contact__item {
    display: flex; align-items: center; height: 34px;
  }
  .contact__icon { width: 18px; height: 18px; margin-right: 32px; }
  .contact__icon svg { width: 18px; height: 18px; fill: var(--accent-blue); display: block; }

  .brand-back {
    position: absolute; left: 118px; top: 132px;
    font-family: "Roboto Condensed", sans-serif; font-weight: 700;
    color: #ffffff; line-height: 1;
  }
  .brand-back__line1 { display: block; font-size: 56px; letter-spacing: -0.5px; }
  .brand-back__line2 { display: block; font-size: 22px; letter-spacing: 28px; margin-top: 10px; }

  .web-address {
    position: absolute; left: 120px; top: 246px;
    font-family: "Roboto", sans-serif; font-weight: 400;
    font-size: 26px; letter-spacing: 2.5px; color: var(--accent-blue-soft);
  }
</style>
</head>
<body>
<main class="sheet">

  <section class="card card--front" aria-label="Business card front">
    <div class="watermark"></div>

    <div class="holder">
      <p class="holder__name">YOUR NAME HERE</p>
      <p class="holder__position">Position</p>
    </div>

    <div class="brand-front">
      <span class="brand-front__mark"></span>
      <p class="brand-front__name">
        <span class="brand-front__line1">LAKEVIEW GLOBAL</span>
        <span class="brand-front__line2">MANAGEMENT</span>
      </p>
    </div>

    <div class="divider"></div>

    <ul class="contact">
      <li class="contact__item">
        <span class="contact__icon"><svg viewBox="0 0 24 24"><path d="M6.6 10.8a15.1 15.1 0 0 0 6.6 6.6l2.2-2.2c.3-.3.7-.4 1-.2 1.1.4 2.3.6 3.6.6.6 0 1 .4 1 1V20c0 .6-.4 1-1 1A17 17 0 0 1 3 4c0-.6.4-1 1-1h3.5c.6 0 1 .4 1 1 0 1.3.2 2.5.6 3.6.1.3 0 .7-.2 1z"/></svg></span>
        +0012 3456 7891
      </li>
      <li class="contact__item">
        <span class="contact__icon"><svg viewBox="0 0 24 24"><path d="M7 3h10v5H7zM4 9h16a2 2 0 0 1 2 2v6h-4v4H6v-4H2v-6a2 2 0 0 1 2-2zm4 6v4h8v-4z"/></svg></span>
        +0012 3456 7891
      </li>
      <li class="contact__item">
        <span class="contact__icon"><svg viewBox="0 0 24 24"><path d="M3 5h18v14H3zm2 2v.5l7 4.5 7-4.5V7z"/></svg></span>
        YOUR ADRESS HERE
      </li>
    </ul>
  </section>

  <section class="card card--back" aria-label="Business card back">
    <div class="watermark"></div>
    <p class="brand-back">
      <span class="brand-back__line1">LAKEVIEW GLOBAL</span>
      <span class="brand-back__line2">MANAGEMENT</span>
    </p>
    <p class="web-address">wwwwww@wwwww.www.com</p>
  </section>

</main>
</body>
</html>
```